Healing Arts Brochure with Simple, Elegant, Zen Design ,

I need to create a brochure for an upcoming event and I have to complete this project in the next few days.
I would like a tri-fold or z fold type of brochure- standard size of 8.5 x 11- both sides with text

i would like the overall design to be simple, elegant and zen .... yet not too plain :-))
I would like the fonts used to be clean and clear and ... easy to read.
I would like the background color to be white/cream or light color
Please do not use too many colors when working with the descriptions of my services or break those sections up too much ... a little is ok.
I don't want the brochure to be busy

I've uploaded the text, my photo, a photo that I will be using on my website, my logo symbol without my name and several logo symbols with my name in different font styles. I am not wed to any of the various font styles of the logo just yet.
TEXT FILE IS UPLOADED

Dear Designers, The design submissions that I'm receiving so far have not been including all 3 pages of text in the brochure. I pulled my text file to update it with the instructions that there are 3 pages of text information that need to be on the brochure. Unfortunately, I'm not able to upload the text file - seems to be a glitch on the ArtMarkly website.. I called for support and they won't get back to me for a couple of hours. That will be around 11:00 am PST in the USA. PLEASE CHECK BACK if you haven't already downloaded the text file. Otherwise, please add the missing information and resubmit your ideas. Thank you!! MR

Target Market(s)

My services target clients in the healing arts.

Industry/Entity Type

Event

Requirements
Must have
• Please include the colors tones of my logo and the sunset photo -golds, oranges, blues
Brochure must include my photo and the sunset photo
Should not have
• Objects like teacups etc. that have nothing to do with my services - thank you kindly
I don't want any other photos or objects on the brochure other than my photo and the sun
Please don't put the tagline in quotes
Please do not make the brochure busy with too many colors in the text.

```html
<!DOCTYPE html>
<html lang="en">
<head>
<meta charset="utf-8">
<title>Healing Arts Brochure – Inside Spread</title>
<link href="https://fonts.googleapis.com/css2?family=Arimo:wght@400;700&display=swap" rel="stylesheet">
<style>
  :root {
    --paper: #fffdec;
    --page-edge: #ffffff;
    --gold: #fcc93a;
    --orange: #f08a1f;
    --deep-orange: #e8672a;
    --blue: #3a5cae;
    --ink: #1e1e1e;
  }
  * { margin: 0; padding: 0; box-sizing: border-box; }
  html, body { width: 1200px; height: 1000px; overflow: hidden; background: var(--page-edge); }
  body { font-family: "Arimo", Arial, sans-serif; color: var(--ink); }

  .spread { position: relative; width: 1200px; height: 1000px; }
  .sheet {
    position: absolute; left: 20px; top: 48px;
    width: 1180px; height: 897px;
    background: var(--paper);
  }
  .swoosh { position: absolute; left: 0; top: 0; }

  .emblem-area {
    position: absolute; left: 20px; top: 60px;
    width: 380px; height: 420px;
    border-radius: 50%;
    background: radial-gradient(circle, rgba(252,201,58,0.20) 0%, rgba(240,200,120,0.10) 50%, rgba(255,253,236,0) 72%);
  }

  .intro { position: absolute; left: 42px; top: 457px; width: 330px; height: 400px; }
  .intro-bar-top { position: absolute; left: 0; top: 0; width: 55px; height: 10px; background: var(--gold); }
  .intro-bar-stem { position: absolute; left: 25px; top: 0; width: 8px; height: 400px; background: var(--gold); }
  .intro-text {
    position: absolute; left: 60px; top: -2px;
    font-size: 22px; line-height: 29.4px;
    color: var(--blue); white-space: nowrap;
  }

  .column {
    position: absolute;
    font-size: 16.2px; line-height: 23px;
    white-space: nowrap;
  }
  .column-middle { left: 448px; top: 189px; }
  .column-right { left: 835px; top: 106px; }
  .column-middle p { margin-bottom: 33px; }
  .column-right p { margin-bottom: 27px; }

  .service-title {
    color: var(--deep-orange);
    font-weight: 400; font-size: 17px; line-height: 23px;
    margin-bottom: 11px;
  }
  .column-right .service-title { margin-top: -3px; margin-bottom: 6px; }

  .column-middle p.lead-in { margin-bottom: 4px; }
  .symptoms { list-style: none; margin: 0 0 25px; }
  .symptoms li { position: relative; padding-left: 24px; }
  .symptoms li::before { content: "•"; position: absolute; left: 2px; top: 0; }
</style>
</head>
<body>
<div class="spread">
  <div class="sheet">
    <svg class="swoosh" width="1180" height="340" viewBox="0 0 1180 340">
      <defs>
        <linearGradient id="sunBand" x1="0" y1="0" x2="1" y2="0">
          <stop offset="0" stop-color="#fcc93a"/>
          <stop offset="0.6" stop-color="#f6a72a"/>
          <stop offset="1" stop-color="#ef8a1d"/>
        </linearGradient>
      </defs>
      <path d="M0 0 H890 C620 20 260 90 0 245 Z" fill="url(#sunBand)"/>
      <path d="M890 0 C600 18 240 95 0 245 L0 282 C250 115 600 25 890 0 Z" fill="var(--blue)"/>
    </svg>

    <div class="emblem-area" role="img" aria-label="Faint brand emblem watermark in gold and soft grey tones"></div>

    <div class="intro">
      <div class="intro-bar-top"></div>
      <div class="intro-bar-stem"></div>
      <p class="intro-text">The services that<br>I offer focus on<br>supporting self-care,<br>self-empowerment<br>and self-regulation.<br>Healing is returning<br>home to our inherent<br>sense of resiliency,<br>vitality and well-being.<br>I am honored to work<br>with you and support<br>you in your own<br>unique journey home<br>to yourself.</p>
    </div>
  </div>

  <section class="column column-middle">
    <h2 class="service-title">Somatic Resourcing™</h2>
    <p>Somatic Resourcing is a body-<br>oriented approach to resolving the<br>symptoms of trauma and chronic<br>stress. Sources of trauma are wide-<br>ranging -- including accidents;<br>falls; surgeries; injuries; physical<br>assault; rape; emotional, physical or<br>sexual abuse; loss of a loved one;<br>childhood neglect or abuse; difficult<br>births; high fever; serious illness;<br>natural disasters, violence and war.</p>
    <p class="lead-in">The symptoms of unresolved trauma<br>can include:</p>
    <ul class="symptoms">
      <li>Panic or anxiety (including panic<br>attacks)</li>
      <li>Hyper-vigilance</li>
      <li>Chronic pain of all kinds</li>
      <li>Sleep disorders</li>
      <li>Chronic tension</li>
      <li>Addictions of all kinds</li>
      <li>Migraines</li>
      <li>Gastrointestinal disorders</li>
      <li>Dissociation</li>
      <li>And many others</li>
    </ul>
    <p>Trauma occurs when the instinctual<br>“high arousal” states of our survival<br>responses (fight, flight and freeze)</p>
  </section>

  <section class="column column-right">
    <p>are unable to discharge, settle and<br>regulate in response to threatening<br>and overwhelming experiences. The<br>result is that this highly charged<br>energy remains stuck or “frozen” as<br>an unresolved memory within the<br>body.</p>
    <p>Somatic Resourcing sessions<br>assist clients to reconnect to their<br>bodies and to gently discharge the<br>stuck or "frozen" energies of trauma<br>so that resiliency, stability and vitality<br>are restored.</p>
    <p>I offer both Somatic Resourcing™<br>bodywork and techniques in my<br>private practice. I’m deeply inspired<br>and grateful for the results that I’ve<br>witnessed in my clients. Somatic<br>Resourcing is remarkable in its<br>ability to bring healing and relief to<br>the fear, hopelessness and pain of<br>trauma.</p>
    <h2 class="service-title">Stillpoint &amp; Yoga Nidra Meditation</h2>
    <p>Stillpoint (Restful Awareness) is<br>a modern adaption of an ancient<br>meditation practice called Yoga<br>Nidra (yogic sleep). Stillpoint is<br>a research based protocol that<br>provides a systematic method for<br>promoting healing, stress reduction<br>and self-regulation. Stillpoint is used</p>
  </section>
</div>
</body>
</html>
```